Project Sign for Construction Company

Site contractor needs a 4'x8' sign to place on construction sites for advertising. Our company builds the infrastructure for new housing developments. These sign will be posted on the road side to be viewed by passing cars. I want a clean and bold look and feel that resembles my company logo.

Font styles to use
Other font styles liked:
• Hypatia Sans Pro

Colors

Designer to choose colors to be used in the design.

Requirements
Must have
• 555-318-2946 | Info@MarlowTerraworks.example
• CUC 8841907
• www.MarlowTerraworks.example
• Services
• Road Construction
• Site Preparation & Excavation
• Underground Utilities
• Shoreline Restoration
Nice to have
• Now Hiring
• Pipe Layers
• Foremen
• Equipment Operators
Should not have
• Should not have stock picture images used in the design, focus on logo and geometric shapes

```html
<!DOCTYPE html>
<html lang="en">
<head>
<meta charset="utf-8">
<title>Marlow Terraworks – Site Sign</title>
<link href="https://fonts.googleapis.com/css2?family=PT+Sans:wght@400;700&display=swap" rel="stylesheet">
<style>
  :root {
    --brand-blue: #1b4c9e;
    --brand-blue-deep: #123a7c;
    --ink: #2e2e2e;
    --paper: #ffffff;
    --silver-light: #f4f4f4;
    --silver-dark: #a9a9a9;
    --band-dark: #1c1c1c;
    --band-mid: #3a3a3a;
  }
  html, body {
    margin: 0;
    padding: 0;
    width: 1200px;
    height: 2499px;
    overflow: hidden;
    background: var(--paper);
  }
  .sign {
    position: relative;
    width: 1200px;
    height: 2499px;
    overflow: hidden;
    background: var(--paper);
    font-family: "PT Sans", sans-serif;
  }
  .photo-worker {
    position: absolute;
    left: 720px; top: 0;
    width: 480px; height: 950px;
    background: linear-gradient(90deg, rgba(255,255,255,0) 0%, #d9d9d9 35%, #9a9a9a 100%);
  }
  .photo-site {
    position: absolute;
    left: 0; top: 1380px;
    width: 1200px; height: 474px;
    background: linear-gradient(90deg, #e6e6e6 0%, #bdbdbd 55%, #8c8c8c 100%);
  }
  .photo-skyline {
    position: absolute;
    left: 760px; top: 900px;
    width: 440px; height: 954px;
    background: linear-gradient(180deg, #d6d6d6 0%, #9e9e9e 60%, #7a7a7a 100%);
  }
  .shapes {
    position: absolute;
    left: 0; top: 0;
    width: 1200px; height: 2499px;
  }
  .brand {
    position: absolute;
    left: 110px; top: 510px;
    color: var(--brand-blue);
    font-weight: 700;
    line-height: 1;
  }
  .brand-name { font-size: 128px; letter-spacing: 4px; }
  .brand-sub { font-size: 50px; letter-spacing: 9px; margin-top: 6px; }
  .services-title {
    position: absolute;
    left: 560px; top: 778px;
    width: 540px;
    text-align: center;
    font-size: 92px;
    font-weight: 700;
    color: var(--ink);
    letter-spacing: 1px;
  }
  .service-list {
    position: absolute;
    left: 262px; top: 0;
    margin: 0; padding: 0;
    list-style: none;
  }
  .service-item {
    position: absolute;
    left: 0;
    white-space: nowrap;
    font-size: 54px;
    font-weight: 700;
    color: var(--paper);
    transform: translateY(-50%);
  }
  .hiring {
    position: absolute;
    left: 0; top: 1880px;
    width: 1200px;
    text-align: center;
    color: var(--paper);
    font-size: 60px;
    line-height: 100px;
  }
  .license {
    position: absolute;
    left: 393px; top: 2118px;
    width: 437px;
    text-align: center;
    font-size: 52px;
    font-weight: 700;
    color: var(--paper);
    line-height: 88px;
  }
  .phone {
    position: absolute;
    left: 250px; top: 2238px;
    font-size: 124px;
    font-weight: 700;
    color: var(--ink);
    line-height: 140px;
    letter-spacing: 2px;
  }
  .contact-line {
    position: absolute;
    left: 0; top: 2386px;
    width: 1200px;
    text-align: center;
    font-size: 32px;
    font-weight: 700;
    color: var(--ink);
    line-height: 44px;
  }
  .contact-line svg { vertical-align: -4px; margin-right: 8px; }
  .contact-line .sep { margin: 0 10px; }
</style>
</head>
<body>
<main class="sign">
  <div class="photo-worker" role="img" aria-label="Photo of a construction worker in a white hard hat seen from behind, with high-rise buildings"></div>
  <div class="photo-skyline" role="img" aria-label="Photo of a city skyline with an elevated road"></div>
  <div class="photo-site" role="img" aria-label="Photo of hands holding a tablet over a site plan"></div>

  <svg class="shapes" viewBox="0 0 1200 2499" aria-hidden="true">
    <defs>
      <linearGradient id="silver" x1="0" y1="0" x2="1" y2="1">
        <stop offset="0" stop-color="#ffffff"/>
        <stop offset="0.55" stop-color="#e3e3e3"/>
        <stop offset="1" stop-color="#9d9d9d"/>
      </linearGradient>
      <linearGradient id="band" x1="0" y1="0" x2="1" y2="0">
        <stop offset="0" stop-color="#151515"/>
        <stop offset="0.5" stop-color="#262626"/>
        <stop offset="1" stop-color="#3d3d3d"/>
      </linearGradient>
      <radialGradient id="iconDisc" cx="0.4" cy="0.35" r="0.7">
        <stop offset="0" stop-color="#ffffff"/>
        <stop offset="1" stop-color="#b8b8b8"/>
      </radialGradient>
    </defs>

    <!-- blue services field -->
    <polygon class="services-field" points="0,755 1180,872 780,1784 0,1584" fill="var(--brand-blue)" opacity="0.93"/>
    <polygon points="1042,952 1180,872 1140,965" fill="var(--brand-blue-deep)"/>

    <!-- silver title banner -->
    <polygon class="services-banner" points="668,727 1162,727 1042,952 500,935" fill="url(#silver)"/>

    <!-- service icons -->
    <g class="service-icons" stroke="#555" stroke-width="4" fill="none" stroke-linecap="round" stroke-linejoin="round">
      <g transform="translate(165,1015)">
        <circle r="58" fill="url(#iconDisc)" stroke="#ffffff" stroke-width="5"/>
        <rect x="-30" y="-20" width="60" height="20"/>
        <line x1="-20" y1="-20" x2="-10" y2="0"/><line x1="0" y1="-20" x2="10" y2="0"/><line x1="20" y1="-20" x2="30" y2="-6"/>
        <line x1="-22" y1="0" x2="-22" y2="28"/><line x1="22" y1="0" x2="22" y2="28"/>
      </g>
      <g transform="translate(165,1160)">
        <circle r="58" fill="url(#iconDisc)" stroke="#ffffff" stroke-width="5"/>
        <rect x="-28" y="0" width="36" height="18" rx="4"/>
        <rect x="-18" y="-20" width="18" height="20"/>
        <path d="M8 4 L22 -22 L32 -6"/>
        <circle cx="-20" cy="24" r="5"/><circle cx="0" cy="24" r="5"/>
      </g>
      <g transform="translate(165,1317)">
        <circle r="58" fill="url(#iconDisc)" stroke="#ffffff" stroke-width="5"/>
        <path d="M-30 18 L0 -22 L30 -22"/>
        <path d="M-22 24 L8 -16 L30 -16"/>
        <line x1="-14" y1="8" x2="2" y2="14"/><line x1="-6" y1="-2" x2="10" y2="4"/>
      </g>
      <g transform="translate(165,1482)">
        <circle r="58" fill="url(#iconDisc)" stroke="#ffffff" stroke-width="5"/>
        <path d="M-24 -26 L-24 10 Q-24 24 -8 24 L16 24"/>
        <path d="M-12 -26 L-12 8 Q-12 12 -6 12 L16 12"/>
        <path d="M6 -22 L6 -8 L26 -8"/>
      </g>
    </g>

    <!-- hiring band -->
    <rect class="hiring-band" x="0" y="1854" width="1200" height="295" fill="url(#band)"/>

    <!-- license tab -->
    <polygon class="license-tab" points="418,2114 830,2114 805,2209 393,2209" fill="var(--brand-blue)"/>

    <!-- phone icon -->
    <g class="phone-icon" transform="translate(178,2310)">
      <circle r="42" fill="none" stroke="var(--ink)" stroke-width="6"/>
      <path d="M-16 -20 Q-26 -10 -16 8 Q-4 26 14 22 L20 12 L8 4 L2 10 Q-8 4 -10 -6 L-4 -10 L-8 -24 Z" fill="var(--brand-blue)"/>
    </g>
  </svg>

  <div class="brand">
    <div class="brand-name">MARLOW</div>
    <div class="brand-sub">TERRAWORKS</div>
  </div>

  <div class="services-title">SERVICES</div>

  <ul class="service-list">
    <li class="service-item" style="top:1015px">Road Construction</li>
    <li class="service-item" style="top:1160px">Site Preparation &amp; Excavation</li>
    <li class="service-item" style="top:1317px">Underground Utilities</li>
    <li class="service-item" style="top:1482px">Shoreline Restoration</li>
  </ul>

  <div class="hiring">
    <div>Now Hiring | Pipe Layers</div>
    <div>Foremen | Equipment Operators</div>
  </div>

  <div class="license">CUC 8841907</div>

  <div class="phone">555-318-2946</div>

  <div class="contact-line">
    <svg width="32" height="24" viewBox="0 0 32 24"><rect x="1" y="1" width="30" height="22" fill="var(--brand-blue)"/><path d="M1 1 L16 13 L31 1" fill="none" stroke="#fff" stroke-width="2"/></svg>Info@MarlowTerraworks.example<span class="sep">|</span><svg width="28" height="28" viewBox="0 0 28 28"><circle cx="14" cy="14" r="12" fill="none" stroke="var(--brand-blue)" stroke-width="3"/><ellipse cx="14" cy="14" rx="5" ry="12" fill="none" stroke="var(--brand-blue)" stroke-width="2"/><line x1="2" y1="14" x2="26" y2="14" stroke="var(--brand-blue)" stroke-width="2"/></svg>www.MarlowTerraworks.example
  </div>
</main>
</body>
</html>
```